Jewelry Wholesale Business Card Design

Company name: VORELLA
Business Background: Wholesale jewelry store located in downtown Los Angeles. We specialize in 18k gold-filled, stainless steel, 14kt gold, and natural stone jewelry.
website: www.vorella-example.com
Instagram: vorella_
Email: sales@vorella-example.com
Address: 318 W. BIRCH AVE #27, #109
LOS ANGELES, CA 90087
(213)555-0147

We would like to create a simple, yet elegant business card for my store
-Includes company logo
-Black background preferred
-Gold metallic color letters
- Lists the type of products we sell
-Small icons for instagram handle, phone, email, and website

Target Market(s)

Hispanic community, age 12-40

Industry/Entity Type

Jewelry Wholesale

Contact Information for Business Card

logo, business location, website, phone number, email, instagram, lists type of products, Dylan Moret(my name)

Font styles to use
Serif
Sans Serif

Colors
FFF300
FFF600
FEFA6F
FFFEC7
FFFEE8

Requirements
Must have
• logo, business location, website, phone number, email, instagram, lists type of products, Dylan Moret(my name)

```html
<!DOCTYPE html>
<html lang="en">
<head>
<meta charset="utf-8">
<title>VORELLA Business Card</title>
<link rel="stylesheet" href="https://fonts.googleapis.com/css2?family=Cinzel:wght@500&family=Poppins:wght@300&family=Montserrat:wght@400;500&display=swap">
<style>
  :root {
    --stage: #5e4a36;
    --card: #030303;
    --gold: #d6ab3c;
    --gold-light: #f3d46a;
    --gold-deep: #a8781f;
    --text-soft: #d2d2d2;
    --text-muted: #9a9a9a;
    --rule: #3a3a3a;
  }
  * { margin: 0; padding: 0; box-sizing: border-box; }
  html, body { width: 900px; height: 1200px; overflow: hidden; }
  body { background: var(--stage); position: relative; }

  .card {
    position: absolute;
    left: 82px;
    width: 733px;
    height: 428px;
    background: var(--card);
    border-radius: 24px;
    overflow: hidden;
    box-shadow: 0 10px 24px rgba(0,0,0,0.45);
  }
  .card--front { top: 137px; }
  .card--back { top: 633px; }

  .brand-name {
    position: absolute;
    font-family: "Cinzel", serif;
    font-weight: 500;
    color: var(--gold);
    line-height: 1;
    letter-spacing: 1px;
    white-space: nowrap;
  }
  .card--front .brand-name { left: 46px; top: 74px; font-size: 64px; }
  .card--back .brand-name { left: 0; right: 0; top: 180px; font-size: 66px; text-align: center; }

  .corner-sweep { position: absolute; top: 0; right: 0; width: 733px; height: 428px; }

  .monogram {
    position: absolute;
    left: 52px; top: 252px;
    width: 122px; height: 134px;
    border-radius: 8px;
    background: linear-gradient(145deg, #e6c27a 0%, #b98a4a 55%, #7a5522 100%);
  }

  .divider {
    position: absolute;
    left: 200px; top: 206px;
    width: 1px; height: 180px;
    background: var(--rule);
  }

  .owner-name {
    position: absolute;
    left: 226px; top: 164px;
    font-family: "Montserrat", sans-serif;
    font-weight: 500;
    font-size: 17px;
    letter-spacing: 2px;
    color: var(--gold);
    white-space: nowrap;
  }

  .contact-list {
    position: absolute;
    left: 226px; top: 202px;
    list-style: none;
    font-family: "Poppins", sans-serif;
    font-weight: 300;
    font-size: 18px;
    color: var(--text-soft);
  }
  .contact-item { display: flex; align-items: center; height: 29.5px; white-space: nowrap; }
  .contact-item svg { width: 17px; height: 17px; margin-right: 12px; flex: none; }
  .contact-item--address { align-items: flex-start; height: auto; margin-top: 17px; font-size: 16.5px; line-height: 29px; }
  .contact-item--address svg { margin-top: 5px; }

  .product-list {
    position: absolute;
    left: 0; right: 0; top: 326px;
    font-family: "Montserrat", sans-serif;
    font-weight: 400;
    font-size: 16.3px;
    letter-spacing: 0.5px;
    color: var(--text-soft);
    text-align: center;
    line-height: 25px;
  }
  .product-list .lead { color: var(--text-muted); }
  .gem { display: inline-block; width: 13px; height: 10px; margin: 0 8px; vertical-align: 0; }

  .back-rule {
    position: absolute;
    left: 46px; right: 43px; top: 380px;
    height: 1px; background: var(--rule);
  }
  .back-site {
    position: absolute;
    left: 0; right: 0; top: 388px;
    font-family: "Montserrat", sans-serif;
    font-weight: 500;
    font-size: 14px;
    letter-spacing: 2px;
    color: var(--gold);
    text-align: center;
  }
</style>
</head>
<body>

<section class="card card--front">
  <svg class="corner-sweep" viewBox="0 0 733 428" aria-hidden="true">
    <defs>
      <linearGradient id="silverBand" x1="0" y1="0" x2="1" y2="0.4">
        <stop offset="0" stop-color="#6f6f6f"/>
        <stop offset="0.55" stop-color="#f4f4f4"/>
        <stop offset="1" stop-color="#9a9a9a"/>
      </linearGradient>
      <linearGradient id="goldBand" x1="0" y1="0" x2="0.6" y2="1">
        <stop offset="0" stop-color="#a8781f"/>
        <stop offset="0.5" stop-color="#f3d46a"/>
        <stop offset="1" stop-color="#c3932c"/>
      </linearGradient>
    </defs>
    <path d="M505 0 L733 0 L733 150 C700 75 615 20 505 0 Z" fill="url(#silverBand)"/>
    <path d="M435 0 C600 18 715 140 733 292 L733 250 C705 120 610 28 478 0 Z" fill="url(#goldBand)"/>
  </svg>

  <h1 class="brand-name">VORELLA</h1>

  <div class="monogram" role="img" aria-label="Brand monogram emblem in rose gold"></div>
  <div class="divider"></div>

  <p class="owner-name">DYLAN MORET</p>

  <ul class="contact-list">
    <li class="contact-item">
      <svg viewBox="0 0 24 24" fill="none" stroke="var(--gold)" stroke-width="2"><path d="M5 3h4l2 5-2.5 1.5a11 11 0 0 0 6 6L16 13l5 2v4a2 2 0 0 1-2 2A17 17 0 0 1 3 5a2 2 0 0 1 2-2z"/></svg>
      (213)555-0147
    </li>
    <li class="contact-item">
      <svg viewBox="0 0 24 24"><rect x="2" y="5" width="20" height="14" rx="1" fill="var(--gold)"/><path d="M2 6l10 7 10-7" fill="none" stroke="#000" stroke-width="1.6"/></svg>
      sales@vorella-example.com
    </li>
    <li class="contact-item">
      <svg viewBox="0 0 24 24" fill="none" stroke="var(--gold)" stroke-width="1.8"><circle cx="12" cy="12" r="9.5"/><ellipse cx="12" cy="12" rx="4" ry="9.5"/><path d="M2.5 12h19M4 7h16M4 17h16"/></svg>
      www.vorella-example.com
    </li>
    <li class="contact-item">
      <svg viewBox="0 0 24 24" fill="none" stroke="var(--gold)" stroke-width="2"><rect x="4" y="4" width="16" height="16" rx="3"/></svg>
      vorella_
    </li>
    <li class="contact-item contact-item--address">
      <svg viewBox="0 0 24 24"><path d="M12 2a7 7 0 0 0-7 7c0 5 7 13 7 13s7-8 7-13a7 7 0 0 0-7-7z" fill="var(--gold)"/><circle cx="12" cy="9" r="2.6" fill="#000"/></svg>
      <span>318 W. BIRCH AVE #27, #109<br>LOS ANGELES, CA 90087</span>
    </li>
  </ul>
</section>

<section class="card card--back">
  <h2 class="brand-name">VORELLA</h2>

  <p class="product-list">
    <span class="lead">BRACELETS</span><svg class="gem" viewBox="0 0 13 10"><path d="M0 3.5L3 0h7l3 3.5L6.5 10z" fill="#d8d8d8"/></svg>EARRINGS<svg class="gem" viewBox="0 0 13 10"><path d="M0 3.5L3 0h7l3 3.5L6.5 10z" fill="#d8d8d8"/></svg><span class="lead">PENDANTS</span><svg class="gem" viewBox="0 0 13 10"><path d="M0 3.5L3 0h7l3 3.5L6.5 10z" fill="#d8d8d8"/></svg>CHAINS<br>
    <span class="lead">CENTENARIOS</span><svg class="gem" viewBox="0 0 13 10"><path d="M0 3.5L3 0h7l3 3.5L6.5 10z" fill="#d8d8d8"/></svg>BANGLES<svg class="gem" viewBox="0 0 13 10"><path d="M0 3.5L3 0h7l3 3.5L6.5 10z" fill="#d8d8d8"/></svg><span class="lead">RINGS</span><svg class="gem" viewBox="0 0 13 10"><path d="M0 3.5L3 0h7l3 3.5L6.5 10z" fill="#d8d8d8"/></svg>ANKLETS<svg class="gem" viewBox="0 0 13 10"><path d="M0 3.5L3 0h7l3 3.5L6.5 10z" fill="#d8d8d8"/></svg>ROSARIES
  </p>

  <div class="back-rule"></div>
  <p class="back-site">WWW.VORELLA-EXAMPLE.COM</p>
</section>

</body>
</html>
```